Pepper Meadow Indian Restaurant - Easter Dinner Buffet

Pepper Meadow is an Indian restaurant located in Perth's northern suburbs. We are offering a Special Easter Dinner buffet which runs during all public holidays.

The key points is
1. 35+ Items on the menu
2. Sea Food ,Goat , Lamb, Chicken Varieties
3. Plenty of options for Vegetarians and Vegans,
4. Available during all Easter Holidays (5:30PM-9:30PM)
5. Only available for Dine In
6. Adult Price $34.50; Kids under 12 eat at $21. Kids under 2 Free

Items on the menu are as below.

S.No Category Item
1 Soup Lentil Soup
2 Veg Starters Saudi Aloo (Potato)
3 Veg Starters Veg Pakora
4 Veg Starters Onion Bhaji
5 Veg Starters Veg Samosa
6 Veg Starters Potato Pakora
7 Veg Starters Chutney Aloo (Potato)
8 NV Starters Tandoori Chicken
9 NV Starters Murg (Chicken) Kali Tikka
10 NV Starters Chicken 65
11 NV Starters Lemon Chicken Tikka
12 Veg Curries Potato Curry
13 Veg Curries Mix Vegetable Curry
14 Veg Curries Mushrool Masala
15 Veg Curries Yellow Dal
16 NV Curries Fish Fry
17 NV Curries Goat Curry
18 NV Curries Butter Chicken
19 NV Curries Lamb Rogan Josh
20 NV Curries Goan Fish Curry
21 NV Curries Special Chicken Curry
22 Rice Prawn Biryani
23 Rice Steamed Rice
24 Rice Saffron Rice
25 Breads Chocolate Naan
26 Breads Butter Naan
27 Breads Garlic Nann
28 Sides Raitha
29 Sides Papadam
30 Sides Salad
31 Dessert Gulab Jamun
32 Dessert Fruit Custard
33 Dessert Semiya Payasam
34 Dessert Coconut Pudding

Industry/Entity Type

Restaurant

Requirements
Must have
• Title
• Easter Buffet - Extravagant Family Buffet

```html
<!DOCTYPE html>
<html lang="en">
<head>
<meta charset="utf-8">
<title>Pepper Meadow Indian Restaurant – Easter Buffet</title>
<link rel="stylesheet" href="https://fonts.googleapis.com/css2?family=Uncial+Antiqua&family=Cormorant+Garamond:ital,wght@1,500;1,600;1,700&display=swap">
<style>
  :root {
    --ink-black: #000000;
    --saffron: #fbb24e;
    --paper: #ffffff;
    --title-red: #e0522a;
    --sub-yellow: #ffe22e;
    --veg-green: #3c6a1c;
    --rice-green: #4d6a28;
    --nv-red: #6a1616;
    --dessert-brown: #5a1a0c;
    --price-red: #ee1c1c;
    --rule: #222222;
  }
  * { margin: 0; padding: 0; box-sizing: border-box; }
  html, body { width: 830px; height: 1200px; overflow: hidden; background: var(--paper); }
  .poster { position: relative; width: 830px; height: 1200px; overflow: hidden; font-family: "Cormorant Garamond", Georgia, serif; font-style: italic; }
  .backdrop { position: absolute; inset: 0; }
  .masthead { position: absolute; left: 0; top: 0; width: 830px; height: 106px; background: var(--ink-black); text-align: center; }
  .masthead-title { font-family: "Uncial Antiqua", serif; font-style: normal; color: var(--title-red); font-size: 44px; line-height: 1; padding-top: 14px; letter-spacing: 1px; }
  .masthead-sub { color: var(--sub-yellow); font-weight: 700; font-size: 18px; margin-top: 12px; }
  .divider { position: absolute; left: 120px; width: 590px; height: 30px; }
  .photo { position: absolute; border-radius: 8px; }
  .menu-list { position: absolute; list-style: none; }
  .menu-list li { white-space: nowrap; }
  .list-starters-veg { left: 38px; top: 268px; font-size: 23px; line-height: 29px; color: var(--veg-green); font-weight: 600; }
  .list-starters-mixed { left: 444px; top: 268px; font-size: 20px; line-height: 25px; font-weight: 600; }
  .list-starters-mixed .veg { color: var(--veg-green); }
  .list-starters-mixed .nv { color: var(--nv-red); }
  .list-curries { left: 38px; top: 575px; font-size: 20.5px; line-height: 25px; color: var(--veg-green); font-weight: 600; }
  .list-rice { left: 448px; top: 575px; font-size: 20.5px; line-height: 25px; color: var(--rice-green); font-weight: 600; }
  .list-desserts { left: 72px; top: 951px; font-size: 20.5px; line-height: 25px; color: var(--dessert-brown); font-weight: 600; }
  .price-band { position: absolute; left: 272px; top: 1087px; width: 558px; height: 40px; background: var(--price-red); color: var(--ink-black); font-size: 19px; font-weight: 600; line-height: 40px; padding-left: 20px; white-space: nowrap; }
  .footer { position: absolute; left: 0; top: 1126px; width: 830px; height: 74px; background: var(--ink-black); color: var(--paper); }
  .footer-hours { text-align: center; font-size: 20px; font-weight: 600; padding-top: 24px; }
  .footer-dinein { position: absolute; right: 14px; bottom: 6px; font-size: 13px; font-weight: 700; }
</style>
</head>
<body>
<div class="poster">
  <svg class="backdrop" width="830" height="1200" viewBox="0 0 830 1200" aria-hidden="true">
    <defs>
      <radialGradient id="chilli-glow" cx="0.55" cy="0.5" r="0.6">
        <stop offset="0" stop-color="#d8401c" stop-opacity="0.75"/>
        <stop offset="0.6" stop-color="#e8702e" stop-opacity="0.4"/>
        <stop offset="1" stop-color="#f4a060" stop-opacity="0"/>
      </radialGradient>
    </defs>
    <polygon points="0,106 830,106 830,118 0,498" fill="var(--saffron)"/>
    <polygon points="130,468 830,455 830,485 0,1045 0,505" fill="var(--saffron)"/>
    <polygon points="830,880 830,1126 470,1126" fill="var(--saffron)"/>
  </svg>

  <div class="photo" role="img" aria-label="Photograph of red dried chillies" style="left:330px;top:700px;width:500px;height:390px;background:radial-gradient(ellipse at 55% 50%, rgba(216,64,28,0.7), rgba(232,112,46,0.35) 55%, rgba(244,160,96,0) 80%);"></div>

  <header class="masthead">
    <h1 class="masthead-title">Pepper Meadow Indian Restaurant</h1>
    <p class="masthead-sub">Easter Buffet - Extravagant Family Buffet</p>
  </header>

  <svg class="divider" style="top:139px" viewBox="0 0 590 30" aria-hidden="true">
    <line x1="4" y1="15" x2="586" y2="15" stroke="var(--rule)" stroke-width="2"/>
    <circle cx="4" cy="15" r="3" fill="var(--rule)"/><circle cx="586" cy="15" r="3" fill="var(--rule)"/>
    <rect x="245" y="3" width="100" height="24" rx="12" fill="var(--saffron)" stroke="var(--rule)" stroke-width="2"/>
  </svg>

  <div class="photo" role="img" aria-label="Photo of fried vegetable starters" style="left:100px;top:198px;width:68px;height:48px;background:linear-gradient(135deg,#8a3a1a,#c46a2a);"></div>
  <div class="photo" role="img" aria-label="Photo of chicken skewers" style="left:186px;top:200px;width:66px;height:46px;background:linear-gradient(135deg,#a8451e,#6a8a30);"></div>
  <div class="photo" role="img" aria-label="Photo of tandoori starter" style="left:536px;top:202px;width:60px;height:42px;background:linear-gradient(135deg,#8a2a10,#b4561e);"></div>
  <div class="photo" role="img" aria-label="Photo of chicken tikka" style="left:632px;top:202px;width:66px;height:42px;background:linear-gradient(135deg,#c08a2a,#8a3a14);"></div>

  <ol class="menu-list list-starters-veg">
    <li>1&nbsp; Soup&nbsp; Lentil Soup</li>
    <li>2&nbsp; Veg Starters Saudi Aloo (Potato)</li>
    <li>3&nbsp; Veg Starters Veg Pakora</li>
    <li>4&nbsp; Veg Starters Onion Bhaji</li>
    <li>5&nbsp; Veg Starters Veg Samosa</li>
    <li>6&nbsp; Veg Starters Potato Pakora</li>
  </ol>

  <ol class="menu-list list-starters-mixed">
    <li class="veg">7&nbsp; Veg Starters Chutney Aloo (Potato)</li>
    <li class="nv">8&nbsp; NV Starters Tandoori Chicken</li>
    <li class="nv">9&nbsp; NV Starters Murg (Chicken) Kali Tikka</li>
    <li class="nv">10&nbsp;&nbsp; NV Starters Chicken 65</li>
    <li class="nv">11&nbsp;&nbsp; NV Starters Lemon Chicken Tikka</li>
  </ol>

  <svg class="divider" style="top:457px" viewBox="0 0 590 30" aria-hidden="true">
    <line x1="4" y1="15" x2="586" y2="15" stroke="var(--rule)" stroke-width="2"/>
    <circle cx="4" cy="15" r="3" fill="var(--rule)"/><circle cx="586" cy="15" r="3" fill="var(--rule)"/>
    <rect x="245" y="3" width="100" height="24" rx="12" fill="var(--paper)" stroke="var(--rule)" stroke-width="2"/>
  </svg>

  <div class="photo" role="img" aria-label="Photo of vegetable curry" style="left:86px;top:516px;width:62px;height:42px;border-radius:50%;background:linear-gradient(135deg,#c4722a,#7a8a2e);"></div>
  <div class="photo" role="img" aria-label="Photo of butter chicken" style="left:158px;top:516px;width:62px;height:42px;border-radius:50%;background:linear-gradient(135deg,#e0602a,#b83a14);"></div>
  <div class="photo" role="img" aria-label="Photo of lamb curry" style="left:230px;top:516px;width:62px;height:42px;border-radius:50%;background:linear-gradient(135deg,#8a4a1a,#5a2a0e);"></div>
  <div class="photo" role="img" aria-label="Photo of naan bread" style="left:480px;top:512px;width:52px;height:42px;border-radius:50%;background:linear-gradient(135deg,#f0dcb0,#c8a46a);"></div>
  <div class="photo" role="img" aria-label="Photo of garlic naan" style="left:540px;top:514px;width:60px;height:40px;border-radius:50%;background:linear-gradient(135deg,#e8c47a,#a8822e);"></div>
  <div class="photo" role="img" aria-label="Photo of paratha" style="left:612px;top:512px;width:56px;height:42px;border-radius:50%;background:linear-gradient(135deg,#e0b870,#9a7430);"></div>

  <ol class="menu-list list-curries">
    <li>12&nbsp;&nbsp; Veg Curries Potato Curry</li>
    <li>13&nbsp;&nbsp; Veg Curries Mix Vegetable Curry</li>
    <li>14&nbsp;&nbsp; Veg Curries Mushrool Masala</li>
    <li>15&nbsp;&nbsp; Veg Curries Yellow Dal</li>
    <li>16&nbsp;&nbsp; NV Curries Fish Fry</li>
    <li>17&nbsp;&nbsp; NV Curries Goat Curry</li>
    <li>18&nbsp;&nbsp; NV Curries Butter Chicken</li>
    <li>19&nbsp;&nbsp; NV Curries Lamb Rogan Josh</li>
    <li>20&nbsp;&nbsp; NV Curries Goan Fish Curry</li>
    <li>21&nbsp;&nbsp; NV Curries Special Chicken Curr</li>
  </ol>

  <ol class="menu-list list-rice">
    <li>22&nbsp;&nbsp; Rice&nbsp;&nbsp; Prawn Biryani</li>
    <li>23&nbsp;&nbsp; Rice&nbsp;&nbsp; Steamed Rice</li>
    <li>24&nbsp;&nbsp; Rice&nbsp;&nbsp; Saffron Rice</li>
    <li>25&nbsp;&nbsp; Breads&nbsp;&nbsp; Chocolate Naan</li>
    <li>26&nbsp;&nbsp; Breads&nbsp;&nbsp; Butter Naan</li>
    <li>27&nbsp;&nbsp; Breads&nbsp;&nbsp; Garlic Nann</li>
    <li>28&nbsp;&nbsp; Sides&nbsp;&nbsp; Raitha</li>
    <li>29&nbsp;&nbsp; Sides&nbsp;&nbsp; Papadam</li>
    <li>30&nbsp;&nbsp; Sides&nbsp;&nbsp; Salad</li>
  </ol>

  <svg class="divider" style="top:839px" viewBox="0 0 590 30" aria-hidden="true">
    <line x1="4" y1="15" x2="586" y2="15" stroke="var(--rule)" stroke-width="2"/>
    <circle cx="4" cy="15" r="3" fill="var(--rule)"/><circle cx="586" cy="15" r="3" fill="var(--rule)"/>
    <rect x="245" y="3" width="100" height="24" rx="12" fill="#f0a868" stroke="var(--rule)" stroke-width="2"/>
  </svg>

  <div class="photo" role="img" aria-label="Photo of payasam dessert bowl" style="left:82px;top:892px;width:66px;height:44px;border-radius:50%;background:linear-gradient(135deg,#f4f0e4,#d8ccb0);"></div>
  <div class="photo" role="img" aria-label="Photo of gulab jamun" style="left:168px;top:888px;width:58px;height:50px;border-radius:50%;background:linear-gradient(135deg,#c05a2a,#7a2a10);"></div>

  <ol class="menu-list list-desserts">
    <li>31&nbsp; Dessert Gulab Jamun</li>
    <li>32&nbsp; Dessert Fruit Custard</li>
    <li>33&nbsp; Dessert Semiya Payasam</li>
    <li>34&nbsp; Dessert Coconut Pudding</li>
  </ol>

  <p class="price-band">Adult Price $34.50; Kids under 12 eat at $21. Kids under 2 Free</p>

  <footer class="footer">
    <p class="footer-hours">Available during all Easter Holidays (5:30pm-9:30pm)</p>
    <p class="footer-dinein">Only available for Dine In</p>
  </footer>
</div>
</body>
</html>
```